Startup in search for creative and funky label for a food product

We, Vindrossa Food Lab need a label for a new product: extra virgin oil from roasted sunflower seeds. The oil is produced at family gardens in sunny Kakheti region in Western Georgia.
Our goal is to introduce this new exclusive product, unknown in Western Europe. The test panels in Sweden liked the product and we hope to sell both for foodies and general public.
The feeling of the label shoud be both creative and exclusive. Maybe even funky, please see the file attached.

We would like to have the label in English and Swedish. Maybe we can do it in English first, since not all of you would understand Swedish, the Swedish design would be identical. The document below has both English and Swedish text.

We attachthe image of the bottle, please do not consider the label on the bottle, it is just an example.

Target Market(s)

General Market in Sweden and Europe. First priority: foddies, restaurants, specialized food stores.

Industry/Entity Type

Online Shopping

Requirements
Must have
• We would need the design in two languages, the same design for Swedish and English, but two separated labels. Once we agree on the English version, we can do the same for Swedish.
Nice to have
• Feeling of locally grown sunflowers, eye-catching.
Should not have
• Classic design for oil

```html
<!DOCTYPE html>
<html lang="en">
<head>
<meta charset="utf-8">
<title>Vindrossa Food Lab – Roasted Sunflower Seed Oil Label</title>
<link rel="stylesheet" href="https://fonts.googleapis.com/css2?family=Almendra+SC&family=Montserrat:wght@700;800&family=Oswald:wght@400;500&display=swap">
<style>
  :root {
    --page: #ffffff;
    --teal-light: #21bcd6;
    --teal: #14a7c3;
    --teal-deep: #0b7f97;
    --navy: #1b2433;
    --circle: #1d1a1c;
    --sun-yellow: #f7c21b;
    --sun-gold: #f0a90e;
    --sun-pale: #fbe36a;
    --lime: #b9c82c;
  }

  * { margin: 0; padding: 0; box-sizing: border-box; }

  html, body {
    width: 1200px;
    height: 2400px;
    overflow: hidden;
    background: var(--page);
  }

  .label {
    position: absolute;
    left: 50px;
    top: 322px;
    width: 1100px;
    height: 1756px;
    overflow: hidden;
    background: linear-gradient(90deg, var(--teal-light) 0%, var(--teal) 55%, var(--teal-deep) 100%);
    text-align: center;
    color: var(--navy);
  }

  .sunflower {
    position: absolute;
    left: 30px;
    top: -40px;
    width: 1040px;
    height: 680px;
    border-radius: 0 0 50% 50% / 0 0 62% 62%;
    background: radial-gradient(ellipse at 50% 20%, var(--sun-pale) 0%, var(--sun-yellow) 45%, var(--sun-gold) 75%, rgba(240, 169, 14, 0) 100%);
  }

  .brand {
    position: absolute;
    left: 366px;
    top: -30px;
    width: 364px;
    height: 364px;
    border-radius: 50%;
    background: var(--circle);
    display: flex;
    align-items: center;
    justify-content: center;
    padding-top: 30px;
  }

  .brand-name {
    font-family: "Oswald", sans-serif;
    font-weight: 400;
    font-size: 50px;
    line-height: 1.1;
    letter-spacing: 2px;
    text-transform: uppercase;
    color: var(--sun-yellow);
  }

  .product-name {
    position: absolute;
    left: 0;
    right: 0;
    top: 700px;
    font-family: "Almendra SC", serif;
    font-weight: 400;
    line-height: 1;
    color: var(--navy);
  }

  .product-name .line-lead {
    display: block;
    font-size: 118px;
    margin-bottom: 18px;
  }

  .product-name .line {
    display: block;
    font-size: 104px;
    margin-bottom: 22px;
  }

  .grade {
    position: absolute;
    left: 0;
    right: 0;
    top: 1250px;
    font-family: "Montserrat", sans-serif;
    font-weight: 800;
    font-size: 70px;
    letter-spacing: 4px;
    color: var(--lime);
  }

  .origin {
    position: absolute;
    left: 0;
    right: 0;
    top: 1340px;
    font-family: "Montserrat", sans-serif;
    font-weight: 800;
    font-size: 31px;
    letter-spacing: 1px;
    color: var(--navy);
  }

  .process {
    position: absolute;
    left: 0;
    right: 0;
    top: 1448px;
    font-family: "Montserrat", sans-serif;
    font-weight: 800;
    font-size: 34px;
    letter-spacing: 2px;
    color: var(--navy);
  }

  .nature {
    position: absolute;
    left: 0;
    right: 0;
    top: 1494px;
    font-family: "Oswald", sans-serif;
    font-weight: 500;
    font-size: 84px;
    line-height: 1;
    letter-spacing: 8px;
    color: var(--lime);
  }

  .volume {
    position: absolute;
    left: 0;
    right: 0;
    top: 1656px;
    font-family: "Montserrat", sans-serif;
    font-weight: 800;
    font-size: 38px;
    color: var(--navy);
  }
</style>
</head>
<body>
  <main class="label">
    <div class="sunflower" role="img" aria-label="Illustration of a bright yellow sunflower bloom across the top of the label"></div>

    <div class="brand">
      <span class="brand-name">Vindrossa<br>Food Lab</span>
    </div>

    <h1 class="product-name">
      <span class="line-lead">Extra Virgin Oil</span>
      <span class="line">from roasted</span>
      <span class="line">sunflower seeds</span>
    </h1>

    <p class="grade">PREMIUM</p>
    <p class="origin">FROM FAMILY GARDENS IN KAKHETI</p>
    <p class="process">—UNREFINED—</p>
    <p class="nature">ALL NATURAL</p>
    <p class="volume">260 ML</p>
  </main>
</body>
</html>
```